R&T Architects - business card and stationary

Aloha,

We have a simple text logo, we need it incorporated into a business card and also stationary design (letterhead) if possible.

Please check out our website, rtamaui-studio.example for a little more about us. The logo we would like to use is in the upper left corner of the website. It is a simple colored logo based on the Klavica font. We are open to new logo's as well, but we want simple.

Thanks

```html
<!DOCTYPE html>
<html lang="en">
<head>
<meta charset="utf-8">
<title>R&amp;T Architects – Business Card</title>
<link rel="stylesheet" href="https://fonts.googleapis.com/css2?family=Noto+Sans:ital,wght@0,400;1,400&display=swap">
<style>
  :root {
    --backdrop: #8d8d8d;
    --card: #ffffff;
    --earth: #6b5b3b;
    --sand: #c4b48f;
    --leaf: #8fad2b;
    --ink: #111111;
  }
  * { margin: 0; padding: 0; box-sizing: border-box; }
  html, body { width: 720px; height: 1200px; overflow: hidden; }
  body {
    background: var(--backdrop);
    font-family: "Noto Sans", sans-serif;
    position: relative;
  }
  .card {
    position: absolute;
    left: 80px; top: 78px;
    width: 561px; height: 1042px;
    background: var(--earth);
    border: 1px solid #000;
  }
  .card-face {
    position: absolute;
    left: 0; top: 0;
    width: 538px; height: 1018px;
    background: var(--card);
  }
  .wordmark {
    position: absolute;
    left: 112px; top: 128px;
    font-size: 42px;
    font-weight: 400;
    color: var(--earth);
    line-height: 1;
    white-space: nowrap;
  }
  .header-rule {
    position: absolute;
    left: 40px; top: 218px;
    width: 521px; height: 3px;
    background: var(--sand);
  }
  .header-rule-accent {
    position: absolute;
    left: 40px; top: 218px;
    width: 57px; height: 9px;
    background: var(--sand);
  }
  .contact-list {
    position: absolute;
    left: 40px; top: 242px;
    list-style: none;
  }
  .contact-list li {
    display: flex;
    align-items: center;
    height: 53px;
    font-size: 28px;
    color: var(--ink);
    line-height: 1;
    white-space: nowrap;
  }
  .contact-list li::before {
    content: "";
    width: 21px; height: 21px;
    background: var(--earth);
    margin-right: 9px;
    flex: none;
  }
  .tagline {
    position: absolute;
    left: 0; top: 674px;
    width: 538px;
    font-style: italic;
    font-size: 30px;
    letter-spacing: 1.8px;
    color: var(--sand);
    line-height: 39px;
    white-space: nowrap;
  }
  .tagline .line-one { display: block; padding-left: 42px; }
  .tagline .line-two { display: block; padding-left: 229px; }
  .tagline-rule {
    position: absolute;
    left: 0; top: 719px;
    width: 179px; height: 2px;
    background: var(--earth);
  }
  .tagline-rule-accent {
    position: absolute;
    left: 179px; top: 719px;
    width: 42px; height: 8px;
    background: var(--earth);
  }
  .website {
    position: absolute;
    left: 0; top: 982px;
    width: 538px;
    text-align: center;
    font-size: 27px;
    color: var(--leaf);
    line-height: 1;
    white-space: nowrap;
  }
</style>
</head>
<body>
  <div class="card">
    <div class="card-face">
      <div class="wordmark">R&amp;T Architects</div>
      <div class="header-rule"></div>
      <div class="header-rule-accent"></div>

      <ul class="contact-list">
        <li class="name">Noa Kahale</li>
        <li class="title">President.CEO</li>
        <li class="phone">p.555.010.2480</li>
        <li class="fax">f.555.010.2481</li>
        <li class="email">noa@rtamaui-studio.example</li>
      </ul>

      <p class="tagline">
        <span class="line-one">environmentally responsible</span>
        <span class="line-two">architechture</span>
      </p>
      <div class="tagline-rule"></div>
      <div class="tagline-rule-accent"></div>

      <div class="website">www.rtamaui-studio.example</div>
    </div>
  </div>
</body>
</html>
```